Need a landing page design updated

Need an existing landing page perfected, want it too look similar to one of Quenbrook's landing pages in that it flows and is really aesthetically pleasing. The link to the landing page is below. I need this design updated asap. Please take the content directly from the page.

http://verdanthollowsx.com/residential-services/

Target Market(s)

High end residential landscape customers on the gulf coast of Florida (Clearwater area)

Industry/Entity Type

Landscape Gardening

Font styles to use
Sans Serif
Decorative

Requirements
Must have
• I want to keep the written content the same on on the landing page, but would like to work on making both aesthetically appealing to the consumer. This is for high end residential clients on the gulf coast of florida, so think palm trees and sunny beaches with beautiful houses and gorgeous landscapes....look through www.verdanthollowsx.com home page for an example of the houses we landscape.
Nice to have
• Would like it to flow as you scroll similar to Quenbrook's landing pages.
• Look at how Quenbrook's landing page flows, want similar here.....
• https://www.quenbrook.com/tavlo-q/
Should not have
• this landing page must be beautiful and must make a lot of sense as you scroll, am looking for a work of art....please do not submit generic templates or anything that can be easily done....I need real artistry.

```html
<!DOCTYPE html>
<html lang="en">
<head>
<meta charset="utf-8">
<title>Residential Landscaping Services</title>
<link rel="stylesheet" href="https://fonts.googleapis.com/css2?family=Quicksand:wght@300;400;500;600;700&display=swap">
<style>
  :root {
    --page-bg: #ffffff;
    --ink: #2f2f2f;
    --ink-soft: #555555;
    --ink-muted: #6e6e6e;
    --accent: #4f8a1c;
    --chevron: #3d6b16;
    --lime-band: #99c900;
    --photo-dark: #1f2a17;
    --photo-mid: #3f6a25;
    --photo-light: #6c9a3a;
    --on-photo: #ffffff;
  }
  * { box-sizing: border-box; margin: 0; padding: 0; }
  html, body { width: 1006px; height: 1200px; overflow: hidden; background: var(--page-bg); }
  body { font-family: "Quicksand", sans-serif; color: var(--ink); position: relative; }

  .comparison { position: absolute; top: 0; left: 0; width: 1006px; height: 428px; }
  .comparison-column { position: absolute; top: 94px; width: 350px; }
  .comparison-column--generic { left: 138px; }
  .comparison-column--tailored { left: 522px; }
  .column-title { font-size: 19.5px; font-weight: 600; letter-spacing: 0.6px; color: var(--ink); line-height: 24px; }
  .title-rule { width: 33px; height: 2px; background: var(--accent); margin-top: 11px; }
  .benefit-list { list-style: none; margin-top: 33px; }
  .benefit-item { position: relative; padding-left: 21px; font-size: 13.2px; line-height: 17px; letter-spacing: 0.5px; color: var(--ink-soft); margin-bottom: 19px; }
  .benefit-item--tight { margin-bottom: 14px; }
  .benefit-item svg { position: absolute; left: 5px; top: 3px; }

  .expertise { position: absolute; top: 428px; left: 0; width: 1004px; height: 334px; overflow: hidden; }
  .expertise-photo { position: absolute; inset: 0;
    background:
      radial-gradient(ellipse 40% 60% at 22% 60%, rgba(30,30,30,0.75), rgba(30,30,30,0) 70%),
      linear-gradient(180deg, #2c3d22 0%, #3b5a26 38%, #5c8a30 62%, #4d7a26 100%); }
  .expertise-shade { position: absolute; inset: 0; background: linear-gradient(90deg, rgba(0,0,0,0) 45%, rgba(10,20,5,0.35) 100%); }
  .expertise-copy { position: absolute; left: 525px; top: 62px; width: 340px; color: var(--on-photo); }
  .expertise-question { font-size: 17px; font-weight: 400; line-height: 17px; letter-spacing: 0.6px; }
  .expertise-rule { width: 33px; height: 2px; background: var(--on-photo); margin: 19px 0 13px; }
  .expertise-text { font-size: 13.2px; line-height: 17px; letter-spacing: 0.6px; font-weight: 500; }
  .expertise-text + .expertise-text { margin-top: 14px; }

  .schedule { position: absolute; top: 826px; left: 0; width: 1006px; text-align: center; }
  .schedule-question { font-size: 14.5px; font-weight: 700; letter-spacing: 1.3px; line-height: 21px; color: var(--ink); }
  .schedule-rule { width: 33px; height: 2px; background: var(--accent); margin: 14px auto 15px; }
  .schedule-answer { font-size: 21px; font-weight: 300; letter-spacing: 1.4px; line-height: 26px; color: var(--ink-muted); }

  .meadow { position: absolute; left: 0; top: 960px; width: 1006px; height: 196px;
    background: linear-gradient(180deg, rgba(120,200,40,0) 0%, rgba(120,200,40,0.35) 30%, #5aaa1e 70%, #3f8a12 100%); }
  .footer-band { position: absolute; left: 0; top: 1156px; width: 1006px; height: 44px; background: var(--lime-band); }
</style>
</head>
<body>

<section class="comparison">
  <div class="comparison-column comparison-column--generic">
    <h2 class="column-title">Generic landscaping services</h2>
    <div class="title-rule"></div>
    <ul class="benefit-list">
      <li class="benefit-item"><svg width="6" height="10" viewBox="0 0 6 10"><path d="M1 1l4 4-4 4" fill="none" stroke="var(--chevron)" stroke-width="1.4"/></svg>You pay for the bundle of services, regardless of whether you actually need them</li>
      <li class="benefit-item"><svg width="6" height="10" viewBox="0 0 6 10"><path d="M1 1l4 4-4 4" fill="none" stroke="var(--chevron)" stroke-width="1.4"/></svg>You get a generic service, not adjusted to the specific needs of your outdoor area</li>
      <li class="benefit-item"><svg width="6" height="10" viewBox="0 0 6 10"><path d="M1 1l4 4-4 4" fill="none" stroke="var(--chevron)" stroke-width="1.4"/></svg>The field team thinks of your property as just another task they have to complete</li>
    </ul>
  </div>
  <div class="comparison-column comparison-column--tailored">
    <h2 class="column-title">Tailor-made landscaping services</h2>
    <div class="title-rule"></div>
    <ul class="benefit-list">
      <li class="benefit-item"><svg width="6" height="10" viewBox="0 0 6 10"><path d="M1 1l4 4-4 4" fill="none" stroke="var(--chevron)" stroke-width="1.4"/></svg>You pay only for the services your yard really needs.</li>
      <li class="benefit-item"><svg width="6" height="10" viewBox="0 0 6 10"><path d="M1 1l4 4-4 4" fill="none" stroke="var(--chevron)" stroke-width="1.4"/></svg>You get your garden’s specific issues solved, and specific requirements met</li>
      <li class="benefit-item benefit-item--tight"><svg width="6" height="10" viewBox="0 0 6 10"><path d="M1 1l4 4-4 4" fill="none" stroke="var(--chevron)" stroke-width="1.4"/></svg>The field team members take their time working on your property</li>
      <li class="benefit-item"><svg width="6" height="10" viewBox="0 0 6 10"><path d="M1 1l4 4-4 4" fill="none" stroke="var(--chevron)" stroke-width="1.4"/></svg>They get to learn all about your vision – and make it a reality</li>
    </ul>
  </div>
</section>

<section class="expertise">
  <div class="expertise-photo" role="img" aria-label="Close-up photo of a lawn mower on a freshly cut green lawn with hedges behind"></div>
  <div class="expertise-shade"></div>
  <div class="expertise-copy">
    <h3 class="expertise-question">Why should you care that Verdant Hollow employs the leading industry experts and uses modern eco-friendly technical solutions?</h3>
    <div class="expertise-rule"></div>
    <p class="expertise-text">That is why we’re able to transform your lawn into a green carpet and get your plants in a perfect health. All while keeping your vision and your&nbsp; budget on our minds.</p>
    <p class="expertise-text">That is why our services actually enable you to reduce the operating expenses.</p>
  </div>
</section>

<section class="schedule">
  <h3 class="schedule-question">Do you worry our services are going to disturb you while trying<br>to unwind in the privacy of your own garden?</h3>
  <div class="schedule-rule"></div>
  <p class="schedule-answer">Our Client Service Operators Build A Schedule Around Your Needs<br>Designed Not To Disturb You At All.</p>
</section>

<div class="meadow" role="img" aria-label="Illustration of tall green grass with butterflies fluttering above it"></div>
<div class="footer-band"></div>

</body>
</html>
```